We have a parent company, Summit Harbor Group (SHG), that has other company partners. We are looking for ways to incorporate our SHG logo with our network partners, Beacon Ledger and The Blue Gate. My initial thought is to have SHG as front of card logo, and include The Blue Gate and Beacon Ledger logos on back but I'm open to ideas. Card should include website www.summitharborgrp.example (use for reference). Keywords "Tax Services" "Real Estate" "Insurance" "Investments" "Chief Financial Officer"

Industry/Entity Type

Financial

```html
<!DOCTYPE html>
<html lang="en">
<head>
<meta charset="utf-8">
<title>Summit Harbor Group – Business Card</title>
<link rel="stylesheet" href="https://fonts.googleapis.com/css2?family=Cinzel:wght@400;600&family=Raleway:wght@400&family=Oswald:wght@400&display=swap">
<style>
  :root {
    --page-bg: #e9e6e1;
    --card-deep: #1d4f98;
    --card-mid: #2a64b3;
    --card-light: #3a78c4;
    --accent-red: #e3272e;
    --ink-light: #f1f1ee;
    --ink-soft: #dfe5ee;
  }
  html, body {
    margin: 0;
    width: 1047px;
    height: 1200px;
    overflow: hidden;
    background: var(--page-bg);
  }
  .card {
    position: absolute;
    left: 266px;
    top: 105px;
    width: 515px;
    height: 940px;
    border-radius: 20px;
    background: radial-gradient(ellipse at 55% 35%, var(--card-light) 0%, var(--card-mid) 45%, var(--card-deep) 100%);
    color: var(--ink-light);
    text-align: center;
    font-family: "Cinzel", serif;
  }
  .card > * { position: absolute; left: 0; right: 0; margin: 0; }
  .brand-mark {
    top: 165px;
    left: 50%;
    right: auto;
    width: 100px;
    height: 100px;
    margin-left: -50px;
    border-radius: 50%;
    background: var(--accent-red);
  }
  .brand-name {
    top: 286px;
    font-size: 31px;
    font-weight: 600;
    letter-spacing: 0.5px;
    white-space: nowrap;
  }
  .partners {
    top: 418px;
    display: flex;
    justify-content: center;
    gap: 34px;
    align-items: flex-start;
  }
  .partner {
    display: flex;
    flex-direction: column;
    align-items: center;
  }
  .partner-name {
    display: flex;
    align-items: center;
    gap: 8px;
    font-size: 19px;
    font-weight: 600;
    white-space: nowrap;
  }
  .partner-dot { width: 22px; height: 22px; border-radius: 50%; background: var(--ink-light); }
  .partner-square { width: 20px; height: 20px; background: var(--ink-light); }
  .partner-tagline {
    margin-top: 6px;
    font-family: "Oswald", sans-serif;
    font-size: 11px;
    color: var(--ink-soft);
    letter-spacing: 0.3px;
    white-space: nowrap;
  }
  .person-name {
    top: 556px;
    font-size: 29px;
    color: var(--accent-red);
    letter-spacing: 1px;
    white-space: nowrap;
  }
  .person-title {
    top: 597px;
    font-size: 23px;
    letter-spacing: 1px;
  }
  .title-rule {
    top: 636px;
    left: 138px;
    right: auto;
    width: 218px;
    height: 2px;
    background: var(--ink-soft);
  }
  .contact {
    font-family: "Raleway", sans-serif;
    font-size: 22px;
    line-height: 33px;
    color: var(--ink-soft);
    white-space: nowrap;
  }
  .contact-address { top: 658px; }
  .contact-lines { top: 734px; }
</style>
</head>
<body>
  <main class="card">
    <div class="brand-mark"></div>
    <div class="brand-name">SUMMIT HARBOR GROUP</div>

    <div class="partners">
      <div class="partner">
        <div class="partner-name"><span class="partner-dot"></span>Beacon Ledger</div>
      </div>
      <div class="partner">
        <div class="partner-name"><span class="partner-square"></span>The Blue Gate</div>
        <div class="partner-tagline">your trusted partner in property</div>
      </div>
    </div>

    <div class="person-name">DANIEL WHITCOMBE</div>
    <div class="person-title">FOUNDER &amp; CEO</div>
    <div class="title-rule"></div>

    <div class="contact contact-address">4820 N Meridian Ave Lakewood,<br>CO 80214</div>
    <div class="contact contact-lines">Tel:720-555-0148<br>Email:info@summitharborgrp.example<br>Web:www.summitharborgrp.example</div>
  </main>
</body>
</html>
```